3 Buttons for Web Site

Hi,

I need three images designed for a web site. They will be used as buttons. If you goto http://www.tarvenmetrix.ie/ you will see three image buttons on the home page. (One of man, one of a family and one of a woman). I need three identical sized buttons, one to have the text "BI Consultancy", one "Managed Near-Shore" and one "QDRX Performance" (Same font etc)

I am thinking of a jigsaw solution, where the text is the missing piece of a puzzle. The rest of the pieces are visible but faint in the background. I would like the back ground of the missing piece to be the same green that is used in the site logo. I attach a basic idea of what I am looking for. Forget about the hand and the piece held by the hand, it is the missing piece that I want the attention on, with some of the surrounding pieces.

I would like the design to blend with the general design of the rest of the site. I am happy to receive 1 PSD and I can do the other two buttons as I will just have to edit the text for those. NB - I use Photoshop elements, not full Photoshop, but that shouldn't make a difference.

I am open to an totally alternative design if you wish.

```html
<!DOCTYPE html>
<html lang="en">
<head>
<meta charset="utf-8">
<title>TarvenMetrix – Services</title>
<link rel="stylesheet" href="https://fonts.googleapis.com/css2?family=Open+Sans:ital,wght@0,400;0,600;0,700;1,400&family=Ubuntu:wght@400&display=swap">
<style>
  :root {
    --page-bg: #e6e6e6;
    --band-bg: #dadada;
    --header-bar: #627074;
    --card-bg: #ffffff;
    --nav-active: #ebebeb;
    --nav-text: #333333;
    --brand-green: #6aa52c;
    --copy-text: #666666;
    --button-bg: #d3d3d3;
    --button-text: #5a6a70;
    --piece-light: #b6ee78;
    --piece-dark: #6ab42e;
  }
  * { box-sizing: border-box; margin: 0; padding: 0; }
  html, body { width: 1200px; height: 674px; overflow: hidden; }
  body {
    position: relative;
    background: var(--page-bg);
    font-family: "Open Sans", Arial, sans-serif;
  }
  .top-band {
    position: absolute; left: 0; top: 40px; width: 1200px; height: 90px;
    background: var(--band-bg);
  }
  .header-bar {
    position: absolute; left: 19px; top: 35px; width: 1099px; height: 99px;
    background: var(--header-bar); border-radius: 4px;
  }
  .brand-card {
    position: absolute; left: 34px; top: 24px; width: 384px; height: 129px;
    background: var(--card-bg); border-radius: 4px;
    box-shadow: 0 3px 8px rgba(0,0,0,.25);
    display: flex; align-items: center; padding-left: 22px; gap: 14px;
  }
  .brand-mark {
    width: 40px; height: 40px; border-radius: 50%; background: var(--brand-green);
  }
  .brand-name {
    font-family: "Open Sans", Arial, sans-serif; font-weight: 700;
    font-size: 36px; color: var(--brand-green); letter-spacing: -.5px;
  }
  .main-nav {
    position: absolute; left: 695px; top: 20px; width: 408px; height: 130px;
    background: var(--card-bg); border-radius: 3px;
    box-shadow: 0 2px 6px rgba(0,0,0,.2);
  }
  .main-nav ul { list-style: none; }
  .nav-item {
    position: absolute; top: 15px; height: 100px; line-height: 100px;
    font-family: "Ubuntu", Arial, sans-serif; font-size: 13px;
    letter-spacing: 1px; color: var(--nav-text);
  }
  .nav-item.is-active {
    left: 16px; width: 94px; text-align: center;
    background: var(--nav-active); border: 1px solid #dddddd; border-radius: 2px;
  }
  .service {
    position: absolute; top: 237px; width: 360px; text-align: center;
  }
  .service-badge {
    position: relative; width: 230px; height: 230px; margin: 0 auto;
    border-radius: 50%;
    background: linear-gradient(180deg, #ffffff 0%, #f2fde6 45%, #c5f79a 100%);
    overflow: hidden;
  }
  .service-badge .piece {
    position: absolute; left: 38px; top: 38px; width: 150px; height: 140px;
    border-radius: 26px;
    background: linear-gradient(160deg, var(--piece-light), var(--piece-dark));
    transform: rotate(-18deg);
  }
  .service-badge .label {
    position: absolute; left: 0; top: 86px; width: 230px;
    font-size: 18px; line-height: 21px; text-align: center;
    transform: rotate(-28deg);
  }
  .label .lead { color: #111111; display: block; }
  .label .trail { color: #ffffff; display: block; }
  .service-copy {
    width: 300px; margin: 38px auto 0; height: 104px;
    font-style: italic; font-size: 18px; line-height: 26px; color: var(--copy-text);
    transform: translateX(var(--copy-shift, 0px));
  }
  .know-more {
    display: block; width: 206px; height: 36px; margin: 12px auto 0;
    background: var(--button-bg); border-radius: 8px;
    font-size: 18px; line-height: 36px; color: var(--button-text);
    text-decoration: none;
    transform: translateX(var(--button-shift, 0px));
  }
</style>
</head>
<body>
  <div class="top-band"></div>
  <div class="header-bar"></div>

  <header class="brand-card">
    <span class="brand-mark"></span>
    <span class="brand-name">TarvenMetrix</span>
  </header>

  <nav class="main-nav">
    <ul>
      <li class="nav-item is-active">SERVICES</li>
      <li class="nav-item" style="left:128px">CLIENTS</li>
      <li class="nav-item" style="left:216px">CONTACT ME</li>
      <li class="nav-item" style="left:339px">BLOG</li>
    </ul>
  </nav>

  <section class="service" style="left:36px; --copy-shift:-8px; --button-shift:-8px">
    <div class="service-badge" role="img" aria-label="Green jigsaw piece with a tick, labelled BI Consultancy">
      <div class="piece"></div>
      <div class="label"><span class="lead">BI</span><span class="trail">Consultancy</span></div>
    </div>
    <p class="service-copy">With 15 years of experience in delivering Business Intelligence Solutions, you can be assured that we will deliver results.</p>
    <a class="know-more" href="#">Know More</a>
  </section>

  <section class="service" style="left:397px; --copy-shift:-8px; --button-shift:-11px">
    <div class="service-badge" role="img" aria-label="Green jigsaw piece with a tick, labelled Managed Near Shore">
      <div class="piece"></div>
      <div class="label"><span class="lead">Managed</span><span class="trail">Near Shore</span></div>
    </div>
    <p class="service-copy">Combine the cost effectiveness of off-shore development with the quality of on-site design and management</p>
    <a class="know-more" href="#">Know More</a>
  </section>

  <section class="service" style="left:744px; --copy-shift:7px; --button-shift:4px">
    <div class="service-badge" role="img" aria-label="Green jigsaw piece with a tick, labelled QDRX Performance">
      <div class="piece"></div>
      <div class="label"><span class="lead">QDRX</span><span class="trail">Performance</span></div>
    </div>
    <p class="service-copy">Get more performance from your Cubeline Services investment. Our tuning solution gets the max from your environment.</p>
    <a class="know-more" href="#">Know More</a>
  </section>
</body>
</html>
```